Agrarhandel benötigt Homepage
Zielgruppe
Wir sind ein Agrarhandel mit einem Warenumschlagslager im Sinne eines klassischen Einzelhandels und vertreiben Produkte an Landwirte.
Wir vertreiben folgende Hauptproduktgruppen:
Einzelfuttermittel
wie z.B. Sojaexktraktionsschrot. Die einzelnen Produkte könnten z.B. wie die Futtermittel auf folgender Seite dargestellt werden (https://www.kornblick.eu/de/produkt/heltrosamin)
Mischfuttermittel
Hier bieten wir unseren Kunden an, individuelles Mischfutter auf Basis unserer Einzelfuttermittel herzustellen.
Weitere Details und weitere Produktbereiche habe ich in einer Powerpoint-Übersicht dargestellt.
Neben diesen Produkten wollen wir uns als Familienunternehmen selbst vorstellen. Zudem betreiben wir in unserer Familie zusätzlich einen Milchviehbetrieb den wir ebenfalls hervorheben möchten, da wir unseren Kunden gegenüber einerseits als Zulieferer aber auch als Kollege auftreten wollen.
Einzelfuttermittel: Hier können wir durch unsere Unabhängigkeit punkten, da wir nicht abhängig von bestimmten Lieferanten sind und dementsprechend unabhängig beraten können. Wir untersuchen im Vergleich zu unseren Wettbewerben die Qualität der Futtermittel bis ins Detail und können daher eine Transparenz bieten, die Konkurrenten in der Regel nicht bieten können. Unser Warenumschlagsplatz mit moderner Technik ermöglicht es uns äußerst kosteneffizient die Waren umschlagen und ausliefern zu können.
Mischfuttermittel: Auf Basis der vorhandenen Einzelfuttermittel stellen wir je nach Kundenwunsch individuelle Mischfutter her. Wir arbeiten mit offenen Deklarationen, sodass unsere Kunden jederzeit nachvollziehen können, ob auch die Einzelfuttermittel verwendet wurden, die sie bestellt haben und keine billigen Ersatzprodukte verwendet wurden.
Zudem sind wir ZP und BRUT zertifiziert. Die aktuellen für unser Unternehmen ausgestellten Zertifikate müssen für unsere Kunden als Download zur Verfügung stehen. Statt dem BRUT-Logo bitte das ..
Aufgabenstellung
Wir möchten gerne ein zeitgemäße Homepage, jedoch muss auch berücksichtigt werden, dass unsere Kunden eher konservativ denken.

```html
<!DOCTYPE html>
<html lang="de">
<head>
<meta charset="utf-8">
<title>Hallmann GmbH – Agrarhandel</title>
<link href="https://fonts.googleapis.com/css2?family=Montserrat:wght@300;400;500;600;700;800;900&display=swap" rel="stylesheet">
<style>
:root{
  --blue:#0b5487;
  --blue-dark:#094a78;
  --gold:#d8a12d;
  --ink:#1f2a33;
  --muted:#5b6470;
  --grey:#efefef;
  --field:#e4e4e4;
  --white:#ffffff;
}
*{box-sizing:border-box;margin:0;padding:0}
html,body{width:1200px;height:5095px;overflow:hidden}
body{font-family:'Montserrat',sans-serif;color:var(--ink);background:var(--white);position:relative}
.abs{position:absolute}
.media{position:absolute;display:block}

/* Hero */
.hero{left:0;top:0;width:1200px;height:658px;background:linear-gradient(180deg,#cfd9c8 0%,#a9bf8f 35%,#6f9a45 62%,#4f7d2c 100%)}
.brand{left:107px;top:42px;font-weight:800;font-size:40px;color:var(--blue);letter-spacing:-.5px;display:flex;align-items:center;gap:12px}
.brand-dot{width:14px;height:14px;border-radius:50%;background:var(--gold)}
.menu{left:1062px;top:64px;width:32px;height:32px;display:grid;grid-template-columns:repeat(3,8px);gap:4px}
.menu span{width:8px;height:8px;border-radius:50%;background:var(--blue)}
.hero-title{left:107px;top:412px;font-size:48px;line-height:49px;color:var(--white);font-weight:300}
.hero-title b{font-weight:800}

/* Story */
.eyebrow{font-size:20px;color:var(--blue);font-weight:400}
.story-eyebrow{left:107px;top:872px}
.story-title{left:107px;top:898px;font-size:34px;font-weight:800;color:var(--blue)}
.story-text{left:107px;top:963px;width:395px;font-size:12px;line-height:24px;color:var(--muted)}
.btn{display:flex;align-items:center;justify-content:center;gap:14px;background:var(--gold);color:var(--white);font-size:11px;font-weight:500;letter-spacing:.3px;border-radius:4px}
.story-btn{left:107px;top:1168px;width:225px;height:68px}
.story-backdrop{left:652px;top:830px;width:425px;height:488px;background:var(--grey);border-radius:22px}
.story-photo{left:672px;top:810px;width:421px;height:491px;border-radius:18px;background:linear-gradient(160deg,#9cb9a0 0%,#5f8f5a 45%,#b53b46 80%,#3f6b3a 100%)}

/* Values */
.values{left:0;top:1453px;width:1200px;height:666px;background:var(--blue)}
.values-mark{left:0;top:1510px;font-size:120px;font-weight:900;color:#0f5f96;letter-spacing:-3px;line-height:1}
.values-intro{left:514px;top:1578px;width:585px;font-size:12px;line-height:24px;color:var(--white)}
.value{width:245px;color:var(--white)}
.value h3{font-size:14px;font-weight:800;line-height:23px;margin-bottom:6px;text-transform:uppercase}
.value p{font-size:12px;line-height:24px}

/* Testimonial */
.arrows{left:548px;top:2248px;display:flex;gap:30px}
.quote{left:130px;top:2288px;width:940px;text-align:center;font-size:36px;line-height:49px;color:#2b2f33;font-weight:400}
.quote b{font-weight:700}
.quote-name{left:0;top:2512px;width:1200px;text-align:center;font-size:14px;font-weight:800;color:var(--blue);letter-spacing:.5px}

/* Social */
.social-bg{left:0;top:3074px;width:1200px;height:1117px;background:var(--grey)}
.photo-dome{left:0;top:2677px;width:378px;height:289px;background:linear-gradient(180deg,#d7e2dc,#7fae70 55%,#9aa59e)}
.photo-vr{left:911px;top:2849px;width:289px;height:241px;background:linear-gradient(180deg,#dfe8ea,#8fae9a 45%,#4f7f3b)}
.photo-field{left:0;top:3193px;width:275px;height:241px;background:linear-gradient(180deg,#7eb557,#4c8a2c)}
.photo-leaves{left:439px;top:3130px;width:425px;height:278px;background:linear-gradient(135deg,#dbe78a,#6aa33a 50%,#2f6a24)}
.social-icon{left:578px;top:2782px}
.social-title{left:0;top:2826px;width:1200px;text-align:center;font-size:36px;line-height:44px;color:var(--blue);font-weight:400}
.social-links{left:561px;top:2937px;display:flex;gap:16px}
.social-links span{width:30px;height:30px;border-radius:50%;background:var(--gold)}

/* Contact */
.contact-title{left:107px;top:3570px;font-size:38px;color:var(--blue);font-weight:400}
.contact-sub{left:107px;top:3618px;font-size:15px;color:#3a3f45}
.field{left:107px;width:583px;background:var(--field);border-radius:8px;font-size:12px;color:#555;padding:18px 26px}
.contact-btn{left:107px;top:4061px;width:170px;height:49px}
.phone-visual{left:731px;top:3677px;width:455px;height:673px}

/* Stats */
.stat{left:107px}
.stat-num{font-size:36px;font-weight:800;color:var(--blue);line-height:40px}
.stat-label{font-size:21px;color:var(--gold);line-height:30px}
.stat-line{left:0;width:490px;height:1px;background:#e6e6e6}
.future-title{left:560px;top:4410px;font-size:36px;color:var(--blue);font-weight:400}
.future-title b{font-weight:800}
.future-text{left:560px;top:4476px;width:540px;font-size:12px;line-height:24px;color:var(--muted)}

/* Footer */
.footer{left:0;top:4730px;width:1200px;height:365px;background:var(--blue)}
.footer-title{left:0;top:4826px;width:1200px;text-align:center;font-size:36px;line-height:45px;color:var(--white);font-weight:400}
.footer-btn{left:488px;top:4923px;width:224px;height:67px}
.footer-line{left:107px;top:5040px;width:986px;height:1px;background:#4f83ab}
.footer-copy{left:107px;top:5058px;font-size:12px;color:var(--white)}
.footer-nav{left:847px;top:5058px;display:flex;gap:24px;font-size:12px;color:var(--white)}
</style>
</head>
<body>

<!-- Hero -->
<section class="hero abs" role="img" aria-label="Foto: Drohne sprüht über ein grünes Feld"></section>
<div class="brand abs">Hallmann<span class="brand-dot"></span></div>
<div class="menu abs"><span></span><span></span><span></span><span></span><span></span><span></span><span></span><span></span><span></span></div>
<h1 class="hero-title abs">Traditionelle <b>Werte,</b><br><b>moderne</b> Lösungen<br>für den <b>Agrarhandel</b></h1>

<!-- Story -->
<div class="story-eyebrow eyebrow abs">Unsere</div>
<h2 class="story-title abs">Geschichte</h2>
<p class="story-text abs">Unser Unternehmen wurde im Jahr 1850 als kleiner, familiengeführter Bauernhof gegründet. Im Laufe der Jahre haben wir uns zu einem der führenden Agrarhandelsunternehmen in Deutschland entwickelt. Wir bieten unseren Kunden eine breite Palette von Produkten und Dienstleistungen an, darunter Einzelfuttermittel, Mischfutter, Saatgut, Silofolien und mehr.</p>
<a class="story-btn btn abs">MEHR ERFAHREN
  <svg width="18" height="10" viewBox="0 0 18 10"><path d="M0 5h16M12 1l4 4-4 4" fill="none" stroke="#fff" stroke-width="1.6"/></svg></a>
<div class="story-backdrop abs"></div>
<div class="story-photo media" role="img" aria-label="Foto: zwei Frauen im Gewächshaus mit Blumen"></div>

<!-- Values -->
<section class="values abs"></section>
<div class="values-mark abs">Hallmann</div>
<p class="values-intro abs">Wir sind ein vertrauenswürdiger Agrarhandel mit einer langen Geschichte, in der wir unseren Kunden die bestmöglichen Produkte und Dienstleistungen anbieten. Wir sind der Innovation und Modernisierung verpflichtet, verlieren aber nie unsere traditionellen Werte der Unabhängigkeit, Neutralität und Kosteneffizienz aus den Augen.</p>
<div class="value abs" style="left:107px;top:1780px"><h3>Modernisierung</h3><p>Neue Technologien und Verfahren haben die Art und Weise, wie Landwirtschaft betrieben wird, grundlegend verändert. Wir sind entschlossen, diesem Wandel mitzugehen und unseren Kunden die modernsten Produkte und Dienstleistungen anzubieten.</p></div>
<div class="value abs" style="left:480px;top:1780px"><h3>Unabhängigkeit &amp;<br>Neutralität</h3><p>Wir sind ein unabhängiges Agrarhandelsunternehmen. Das bedeutet, dass wir nicht an bestimmte Lieferanten oder Hersteller gebunden sind. Dadurch können wir unseren Kunden die besten Produkte zu den besten Preisen anbieten.</p></div>
<div class="value abs" style="left:854px;top:1780px"><h3>Kosteneffizienz</h3><p>Wir bieten unseren Kunden wettbewerbsfähige Preise und attraktive Rabatte. Außerdem bieten wir unseren Kunden eine Reihe von Wert-Added-Services an, wie z. B. kostenlose Beratung und Lieferung.</p></div>

<!-- Testimonial -->
<div class="arrows abs">
  <svg width="34" height="16" viewBox="0 0 34 16"><path d="M33 8H2M8 2L2 8l6 6" fill="none" stroke="#c9c9c9" stroke-width="2"/></svg>
  <svg width="34" height="16" viewBox="0 0 34 16"><path d="M1 8h31M26 2l6 6-6 6" fill="none" stroke="#d8a12d" stroke-width="2"/></svg>
</div>
<blockquote class="quote abs">"Ich bin sehr beeindruckt von der Qualität der Produkte und der Professionalität des Teams bei <b>Hallmann GmbH</b>. Ich kann dieses Unternehmen nur wärmstens empfehlen."</blockquote>
<div class="quote-name abs">JONAS BERGER</div>

<!-- Social -->
<div class="social-bg abs"></div>
<div class="photo-dome media" role="img" aria-label="Bild: Pflanzen unter einer Glaskuppel im Labor"></div>
<div class="photo-vr media" role="img" aria-label="Foto: Landwirt mit VR-Brille im Gewächshaus"></div>
<div class="photo-field media" role="img" aria-label="Bild: Person im Feld mit digitaler Einblendung"></div>
<div class="photo-leaves media" role="img" aria-label="Bild: Hand an Pflanzen mit Datennetz-Grafik"></div>
<svg class="social-icon abs" width="44" height="42" viewBox="0 0 44 42"><path d="M22 40V8M22 20l-10-8M22 20l10-8M22 30l-14-8M22 30l14-8" fill="none" stroke="#0b5487" stroke-width="2" stroke-linecap="round"/><line x1="8" y1="40" x2="36" y2="40" stroke="#0b5487" stroke-width="2"/></svg>
<h2 class="social-title abs">Folgen Sie uns<br>auf Social Media</h2>
<div class="social-links abs"><span></span><span></span></div>

<!-- Contact -->
<h2 class="contact-title abs">Kontaktieren uns</h2>
<p class="contact-sub abs">Haben Sie eine Frage oder möchten Sie ein Angebot einholen?</p>
<div class="field abs" style="top:3673px;height:52px">Name</div>
<div class="field abs" style="top:3744px;height:52px">E-Mail-Adresse</div>
<div class="field abs" style="top:3818px;height:51px">Telefonnummer</div>
<div class="field abs" style="top:3889px;height:134px">Nachricht</div>
<a class="contact-btn btn abs">SENDEN</a>
<svg class="phone-visual" role="img" aria-label="Bild: Smartphone mit grünen Feldreihen" viewBox="0 0 455 673">
  <defs><linearGradient id="phoneFill" x1="0" y1="0" x2="0" y2="1"><stop offset="0" stop-color="#cfe9f5"/><stop offset=".4" stop-color="#9fcf7a"/><stop offset="1" stop-color="#2f6a24"/></linearGradient></defs>
  <path d="M215 10 L445 30 L260 520 L20 520 Z" fill="url(#phoneFill)"/>
  <ellipse cx="230" cy="640" rx="110" ry="12" fill="#e8e8e8"/>
</svg>

<!-- Stats -->
<div class="stat abs" style="top:4325px"><div class="stat-num">24</div><div class="stat-label">Jahre Erfahrung</div></div>
<div class="stat-line abs" style="top:4412px"></div>
<div class="stat abs" style="top:4442px"><div class="stat-num">98%</div><div class="stat-label">Positive Bewertungen</div></div>
<div class="stat-line abs" style="top:4530px"></div>
<div class="stat abs" style="top:4560px"><div class="stat-num">500+</div><div class="stat-label">Zufriedene Kunden</div></div>
<h2 class="future-title abs">Der Agrarhandel der <b>Zukunft</b></h2>
<p class="future-text abs">Die Landwirtschaft steht vor großen Herausforderungen: Klimawandel, Bevölkerungswachstum und Ressourcenknappheit. Wir müssen neue Wege finden, um Nahrungsmittel sicher und nachhaltig zu produzieren.</p>

<!-- Footer -->
<footer class="footer abs" role="img" aria-label="Blauer Abschluss mit Grassilhouette am oberen Rand"></footer>
<h2 class="footer-title abs">Ihr Partner für eine<br>erfolgreiche Landwirtschaft</h2>
<a class="footer-btn btn abs">JETZT LOSLEGEN
  <svg width="18" height="10" viewBox="0 0 18 10"><path d="M0 5h16M12 1l4 4-4 4" fill="none" stroke="#fff" stroke-width="1.6"/></svg></a>
<div class="footer-line abs"></div>
<div class="footer-copy abs">© 2023 Hallmann GmbH</div>
<nav class="footer-nav abs"><span>Impressum</span><span>Datenschutz</span><span>Kontakt</span></nav>

</body>
</html>
```